PowerPoint template for my training workshop business

I would like to have a PowerPoint template created using my logo and palette materials created by Brivantelox. I train and facilitate workshops using PowerPoint in both corporate and public settings.

I have attached the original design elements to this request.

```html
<!DOCTYPE html>
<html lang="en">
<head>
<meta charset="utf-8">
<title>Marisol Keane Coaching – Slide Template</title>
<link href="https://fonts.googleapis.com/css2?family=Montserrat:wght@700;800&family=Mulish:wght@400;600;700&family=Merriweather:wght@700&display=swap" rel="stylesheet">
<style>
:root{
  --orange:#f7a21b;
  --orange-light:#fdbb2d;
  --orange-deep:#f08a0c;
  --gold:#e7b640;
  --dark:#1d1d1f;
  --dark-2:#2b2b2e;
  --footer:#4a4a4c;
  --paper:#fdfaf5;
  --white:#ffffff;
  --ink:#2a2a2a;
  --muted:#a9a9a9;
  --grey-ring:#9aa0b4;
}
*{margin:0;padding:0;box-sizing:border-box}
html,body{width:1051px;height:1200px;overflow:hidden;background:#000}
body{position:relative;font-family:"Mulish",sans-serif;color:var(--ink)}
.slide{position:absolute;width:502px;height:282px;overflow:hidden;background:var(--white)}
.col-a{left:10px}.col-b{left:530px}
.row-1{top:13px}.row-2{top:308px}.row-3{top:608px}.row-4{top:909px}
.abs{position:absolute}

/* shared chrome */
.header{position:absolute;left:0;top:0;width:100%;height:38px;background:linear-gradient(180deg,var(--orange-light),var(--orange))}
.header h2{position:absolute;left:11px;top:10px;font-family:"Montserrat",sans-serif;font-weight:800;font-size:16px;color:var(--dark);letter-spacing:.2px}
.brand-tab{position:absolute;right:0;top:0;width:150px;height:38px;background:var(--dark-2);clip-path:polygon(14% 0,100% 0,100% 100%,24% 100%)}
.brand{position:absolute;display:flex;align-items:center;gap:5px}
.brand-dot{border-radius:50%;border:2px solid var(--orange);flex:none}
.brand-name{font-family:"Mulish",sans-serif;font-weight:700;color:var(--gold);line-height:1;white-space:nowrap}
.brand-sub{display:block;font-size:.45em;letter-spacing:2px;color:var(--gold);margin-top:2px;text-align:center}
.header .brand{right:9px;top:9px}
.header .brand-dot{width:19px;height:19px}
.header .brand-name{font-size:9.5px}
.footer{position:absolute;left:0;bottom:0;width:100%;height:12px;background:var(--footer)}
.footer span{position:absolute;left:3px;top:2px;font-size:6px;font-weight:700;color:var(--white)}
.page-no{position:absolute;right:6px;bottom:5px;width:21px;height:21px;border-radius:50%;background:var(--orange);border:2px solid var(--white);font-size:6.5px;font-weight:700;color:var(--white);display:flex;align-items:center;justify-content:center}

.photo{position:absolute;background:linear-gradient(135deg,#d9d4cc,#8b8f96 55%,#2b2b2e)}
.photo-round{border-radius:50%;border:3px solid var(--orange-light)}
.img-title{font-family:"Montserrat",sans-serif;font-weight:700;font-size:13.5px;color:var(--orange)}
.body{font-size:7.6px;line-height:1.65;color:#555}
.para-title{font-family:"Merriweather",serif;font-weight:700;color:var(--orange)}
.muted{color:var(--muted)}
.on-dark{color:#e8e8e8}

/* title slide */
.cover{background:var(--orange)}
.cover-top{position:absolute;left:0;top:0;width:100%;height:223px;background:radial-gradient(circle at 80% 40%,var(--orange-light),var(--orange) 60%,var(--orange-deep))}
.cover-bottom{position:absolute;left:0;top:223px;width:100%;height:59px;background:var(--dark)}
.cover h1{position:absolute;right:24px;top:80px;text-align:right;font-family:"Montserrat",sans-serif;font-weight:800;font-size:30px;line-height:1.1;color:var(--dark)}
.cover .sub{position:absolute;right:24px;top:168px;font-family:"Montserrat",sans-serif;font-weight:700;font-size:11px;color:var(--dark)}
.cover .rule{position:absolute;left:290px;right:24px;top:160px;height:1px;background:rgba(0,0,0,.25)}
.cover .who{position:absolute;left:53px;width:130px;top:194px;text-align:center;font-family:"Montserrat",sans-serif;font-weight:700;color:var(--dark);line-height:1.2}
.cover .who b{display:block;font-size:9.5px}
.cover .who small{display:block;font-size:7px}
.cover .brand{left:298px;top:238px}
.cover .brand-dot{width:36px;height:36px}
.cover .brand-name{font-size:16px}

/* stats */
.stat{position:absolute;width:88px;height:88px;border-radius:50%;background:radial-gradient(circle,#d9a52a,#b98712);border:3px solid #e1b23a;display:flex;flex-direction:column;align-items:center;justify-content:center;gap:4px}
.stat b{font-size:8.5px;color:var(--dark)}
.caption{position:absolute;width:110px;text-align:center;font-size:7.6px;line-height:1.6;color:#e8e8e8}

/* valuation */
.valuation{position:absolute;left:325px;top:84px;width:132px;height:132px;border-radius:50%;border:3px solid var(--grey-ring);padding:4px}
.valuation div{width:100%;height:100%;border-radius:50%;background:var(--orange);display:flex;flex-direction:column;align-items:center;justify-content:center;color:var(--white);font-size:15px;line-height:1.25;text-align:center}
.valuation strong{font-family:"Montserrat",sans-serif;font-size:22px;font-weight:800}
.dot{position:absolute;border-radius:50%}
</style>
</head>
<body>

<!-- Cover -->
<section class="slide cover col-a row-1">
  <div class="cover-top"></div>
  <div class="cover-bottom"></div>
  <div class="photo photo-round" role="img" aria-label="Portrait photo of the coach" style="left:50px;top:39px;width:136px;height:136px;border:4px solid var(--orange-light);background:linear-gradient(160deg,#c9b7a4,#6a5547 60%,#3b2f29)"></div>
  <h1>PERSENTATION<br>TITLE HERE</h1>
  <div class="rule"></div>
  <p class="sub">SUBTEXT HERE SUBTEXT HERE</p>
  <p class="who"><b>MARISOL KEANE</b><small>LIFE COACH</small></p>
  <div class="brand"><span class="brand-dot"></span><span class="brand-name">MARISOL KEANE<span class="brand-sub">COACHING</span></span></div>
</section>

<!-- Two images -->
<section class="slide col-b row-1" style="background:var(--paper)">
  <header class="header"><h2>PROJECT TITLE HERE</h2><div class="brand-tab"></div><div class="brand"><span class="brand-dot"></span><span class="brand-name">MARISOL KEANE<span class="brand-sub">COACHING</span></span></div></header>
  <div class="photo photo-round" role="img" aria-label="Photo of a woman stretching" style="left:71px;top:62px;width:96px;height:96px"></div>
  <div class="photo photo-round" role="img" aria-label="Photo of a woman stretching" style="left:307px;top:62px;width:96px;height:96px"></div>
  <p class="img-title abs" style="left:0;width:238px;top:176px;text-align:center">IMAGE TITLE HERE</p>
  <p class="body abs" style="left:31px;width:176px;top:194px;text-align:center">Do you have a business presentation PowerPoint to give this week? Or, is the deadline for your pitch approaching fast? Or, is the clock ticking down to the date of your speaking engagement?</p>
  <p class="img-title abs" style="left:236px;width:238px;top:176px;text-align:center">IMAGE TITLE HERE</p>
  <p class="body abs" style="left:267px;width:176px;top:194px;text-align:center">Do you have a business presentation PowerPoint to give this week? Or, is the deadline for your pitch approaching fast? Or, is the clock ticking down to the date of your speaking engagement?</p>
  <div class="footer"><span>Copyright text here</span></div><div class="page-no">01</div>
</section>

<!-- Blank -->
<section class="slide col-a row-2">
  <header class="header"><h2>PROJECT TITLE HERE</h2><div class="brand-tab"></div><div class="brand"><span class="brand-dot"></span><span class="brand-name">MARISOL KEANE<span class="brand-sub">COACHING</span></span></div></header>
  <div class="footer"><span>Copyright text here</span></div><div class="page-no">01</div>
</section>

<!-- Stats over photo -->
<section class="slide col-b row-2">
  <div class="photo" role="img" aria-label="Dimmed background photo of a woman stretching outdoors" style="left:0;top:38px;width:502px;height:232px;background:linear-gradient(120deg,#2a2a2c,#4a4744 45%,#2a2a2c)"></div>
  <header class="header"><h2>PROJECT TITLE HERE</h2><div class="brand-tab"></div><div class="brand"><span class="brand-dot"></span><span class="brand-name">MARISOL KEANE<span class="brand-sub">COACHING</span></span></div></header>
  <div class="stat" style="left:47px;top:102px">
    <svg width="18" height="36" viewBox="0 0 18 36" aria-hidden="true"><circle cx="9" cy="4" r="4" fill="#1d1d1f"/><path d="M4 10h10l3 14h-4v11h-3V25h-2v10H5V24H1z" fill="#1d1d1f"/></svg>
    <b>1.9 Billion</b>
  </div>
  <div class="stat" style="left:186px;top:102px">
    <svg width="18" height="36" viewBox="0 0 18 36" aria-hidden="true"><circle cx="9" cy="4" r="4" fill="#1d1d1f"/><path d="M4 10h10l3 14h-4v11h-3V25h-2v10H5V24H1z" fill="#1d1d1f"/></svg>
    <b>1.9 Billion</b>
  </div>
  <p class="caption" style="left:36px;top:200px">Do you have a business presentation PowerPoint to give this week</p>
  <p class="caption" style="left:175px;top:200px">Do you have a business presentation PowerPoint to give this week</p>
  <p class="para-title abs" style="left:330px;top:69px;font-size:13px">Paragraph Title here</p>
  <p class="body on-dark abs" style="left:330px;top:95px;width:155px">Do you have a business presentation PowerPoint to give this week? Is the deadline for your pitch approaching fast? Or, is the clock ticking down to the date of your speaking engagement?<br><br>Do you have a business presentation PowerPoint to give this week? Is the deadline for your pitch approaching fast? Or, is the clock ticking down to the date of your speaking engagement?</p>
  <div class="footer"><span>Copyright text here</span></div><div class="page-no">01</div>
</section>

<!-- Text + photo -->
<section class="slide col-a row-3">
  <header class="header"><h2>PROJECT TITLE HERE</h2><div class="brand-tab"></div><div class="brand"><span class="brand-dot"></span><span class="brand-name">MARISOL KEANE<span class="brand-sub">COACHING</span></span></div></header>
  <div class="abs" style="left:0;top:38px;width:226px;height:232px;background:var(--dark)"></div>
  <div class="photo" role="img" aria-label="Photo of a woman stretching against a wall by the sea" style="left:226px;top:38px;width:276px;height:232px;background:linear-gradient(135deg,#cfd6dc,#e9e6e1 45%,#8d8a86 75%,#2a2a2c)"></div>
  <p class="para-title abs" style="left:25px;top:60px;font-size:15px">Paragraph Title here</p>
  <p class="body on-dark abs" style="left:25px;top:86px;width:190px">Do you have a business presentation PowerPoint to give this week? Is the deadline for your pitch approaching fast? Or, is the clock ticking down to the date of your speaking engagement?<br><br>Do you have a business presentation PowerPoint to give this week? Is the deadline for your pitch approaching fast? Or, is the clock ticking down to the date of your speaking engagement?<br><br>If so, your needs are immediate. It's critical that you create a professional presentation that's designed for business results.</p>
  <div class="footer"><span>Copyright text here</span></div><div class="page-no">01</div>
</section>

<!-- Valuation -->
<section class="slide col-b row-3">
  <header class="header"><h2>PROJECT TITLE HERE</h2><div class="brand-tab"></div><div class="brand"><span class="brand-dot"></span><span class="brand-name">MARISOL KEANE<span class="brand-sub">COACHING</span></span></div></header>
  <p class="para-title abs" style="left:32px;top:76px;font-size:18px">Paragraph Title here</p>
  <p class="body muted abs" style="left:33px;top:108px;width:250px">Do you have a business presentation PowerPoint to give this week? Is the deadline for your pitch approaching fast? Or, is the clock ticking down to the date of your speaking engagement?<br><br>Do you have a business presentation PowerPoint to give this week? Is the deadline for your pitch approaching fast? Or, is the clock ticking down to the date of your speaking engagement?<br><br>If so, your needs are immediate. It's critical that you create a professional presentation that's designed for business results.</p>
  <div class="valuation"><div><span>OUR<br>VALUATION</span><strong>100 MN</strong></div></div>
  <span class="dot" style="left:419px;top:83px;width:27px;height:27px;background:var(--orange-light)"></span>
  <span class="dot" style="left:347px;top:201px;width:14px;height:14px;background:#c9c9c9"></span>
  <div class="footer"><span>Copyright text here</span></div><div class="page-no">01</div>
</section>

<!-- Text + figure -->
<section class="slide col-a row-4">
  <header class="header"><h2>PROJECT TITLE HERE</h2><div class="brand-tab"></div><div class="brand"><span class="brand-dot"></span><span class="brand-name">MARISOL KEANE<span class="brand-sub">COACHING</span></span></div></header>
  <p class="para-title abs" style="left:32px;top:76px;font-size:18px">Paragraph Title here</p>
  <p class="body muted abs" style="left:33px;top:108px;width:250px">Do you have a business presentation PowerPoint to give this week? Is the deadline for your pitch approaching fast? Or, is the clock ticking down to the date of your speaking engagement?<br><br>Do you have a business presentation PowerPoint to give this week? Is the deadline for your pitch approaching fast? Or, is the clock ticking down to the date of your speaking engagement?<br><br>If so, your needs are immediate. It's critical that you create a professional presentation that's designed for business results.</p>
  <span class="dot" style="left:351px;top:111px;width:80px;height:80px;background:var(--orange-deep)"></span>
  <span class="dot" style="left:430px;top:96px;width:33px;height:33px;background:#fcc02c"></span>
  <span class="dot" style="left:352px;top:194px;width:13px;height:13px;background:#cfcfcf"></span>
  <div class="photo" role="img" aria-label="Cut-out photo of a woman in a standing yoga pose" style="left:330px;top:58px;width:92px;height:188px;border-radius:40px;background:linear-gradient(180deg,rgba(120,220,210,.85),rgba(60,60,64,.85) 55%,rgba(110,210,200,.85));"></div>
  <div class="footer"><span>Copyright text here</span></div><div class="page-no">01</div>
</section>

<!-- Image list -->
<section class="slide col-b row-4" style="background:var(--paper)">
  <header class="header"><h2>PROJECT TITLE HERE</h2><div class="brand-tab"></div><div class="brand"><span class="brand-dot"></span><span class="brand-name">MARISOL KEANE<span class="brand-sub">COACHING</span></span></div></header>
  <p class="img-title abs" style="left:23px;top:69px">IMAGE TITLE HERE</p>
  <p class="body abs" style="left:23px;top:86px;width:350px;color:#444">Do you have a business presentation PowerPoint to give this week? Is the deadline for your pitch approaching fast? Or, is the clock ticking down to the date of your speaking engagement? Do you have a business presentation PowerPoint to give this week? Is the deadline for your pitch approaching fast? Or, is the clock ticking down to the date of your speaking engagement?</p>
  <p class="img-title abs" style="left:23px;top:175px">IMAGE TITLE HERE</p>
  <p class="body abs" style="left:23px;top:192px;width:350px;color:#444">Do you have a business presentation PowerPoint to give this week? Is the deadline for your pitch approaching fast? Or, is the clock ticking down to the date of your speaking engagement? Do you have a business presentation PowerPoint to give this week? Is the deadline for your pitch approaching fast? Or, is the clock ticking down to the date of your speaking engagement?</p>
  <div class="photo photo-round" role="img" aria-label="Photo of a woman stretching" style="left:380px;top:65px;width:86px;height:86px"></div>
  <div class="photo photo-round" role="img" aria-label="Photo of a woman stretching" style="left:380px;top:170px;width:86px;height:86px"></div>
  <div class="footer"><span>Copyright text here</span></div><div class="page-no">01</div>
</section>

</body>
</html>
```